Presentation Folder, Business Card, Letterhead and Envelope design

We are a dental clinic that will open in August and we are looking for a professional graphic designer to create our Business Card, Presentation Folder, Letterhead, Notepad and envelopes.

The brand NovaGrin must reflect a sense of quality and sophistication, marketed for middle-class consumers.
Our preference is for quality and refined materials, where less is more.
Attached the logo

```html
<!DOCTYPE html>
<html lang="en">
<head>
<meta charset="utf-8">
<title>NovaGrin Letterhead</title>
<link href="https://fonts.googleapis.com/css2?family=Roboto:wght@300;400&display=swap" rel="stylesheet">
<style>
  :root {
    --backdrop: #dedede;
    --paper: #fafafa;
    --ink-grey: #6a6a6a;
    --brand-red: #7e2b30;
    --brand-grey: #666666;
  }
  * { margin: 0; padding: 0; box-sizing: border-box; }
  html, body {
    width: 1200px;
    height: 800px;
    overflow: hidden;
    background: var(--backdrop);
  }
  .canvas {
    position: relative;
    width: 1200px;
    height: 800px;
    display: flex;
    align-items: center;
    justify-content: center;
  }
  .letterhead {
    position: relative;
    width: 540px;
    height: 760px;
    background: var(--paper);
    font-family: "Roboto", Arial, sans-serif;
  }
  .brand {
    position: absolute;
    left: 55px;
    top: 69px;
    display: flex;
    align-items: center;
    gap: 10px;
  }
  .brand-square {
    width: 28px;
    height: 28px;
    background: var(--brand-grey);
  }
  .brand-name {
    font-family: "Roboto", Arial, sans-serif;
    font-weight: 300;
    font-size: 29px;
    line-height: 1;
    letter-spacing: 6px;
    text-transform: uppercase;
    color: var(--brand-grey);
  }
  .contact {
    position: absolute;
    left: 55px;
    top: 689px;
    font-size: 10.5px;
    font-weight: 400;
    color: var(--ink-grey);
    line-height: 15.5px;
  }
  .contact-line {
    display: flex;
    align-items: center;
    white-space: nowrap;
  }
  .contact-item {
    display: inline-flex;
    align-items: center;
    gap: 3px;
    margin-right: 5px;
  }
  .contact-icon {
    width: 8px;
    height: 8px;
    fill: var(--brand-red);
  }
</style>
</head>
<body>
<main class="canvas">
  <article class="letterhead">
    <header class="brand">
      <div class="brand-square"></div>
      <span class="brand-name">NovaGrin</span>
    </header>

    <footer class="contact">
      <p class="contact-line">48 Maple Crest Avenue,&nbsp; Oakridge, ON L5T 3K8</p>
      <p class="contact-line">
        <span class="contact-item">
          <svg class="contact-icon" viewBox="0 0 10 10" aria-hidden="true">
            <path d="M1 3.2C1 2 2.5 1.2 5 1.2S9 2 9 3.2V4H7V3.3H3V4H1Z"/>
            <path d="M2.5 4.4H7.5L8.8 8.8H1.2Z"/>
          </svg>
          020 7946 0182
        </span>
        <span class="contact-item">
          <svg class="contact-icon" viewBox="0 0 10 10" aria-hidden="true">
            <path d="M0.5 2H9.5V8H0.5Z"/>
            <path d="M0.8 2.3L5 5.6L9.2 2.3" fill="none" stroke="#fafafa" stroke-width="0.8"/>
          </svg>
          clara@novagrinmail.com
        </span>
        <span class="contact-item">
          <svg class="contact-icon" viewBox="0 0 10 10" aria-hidden="true">
            <circle cx="5" cy="5" r="4.5"/>
            <path d="M3 2.2C4.2 2.8 3.6 4 4.6 4.6S5.2 6.4 4.2 7.8M6.4 2C6 3 7 3.6 7.8 4" fill="none" stroke="#fafafa" stroke-width="0.8"/>
          </svg>
          www.novagrinweb.com
        </span>
      </p>
    </footer>
  </article>
</main>
</body>
</html>
```